Irrigation Business needs their business cards modernised and revamped

I would like to keep my current logo, colours and revamp the format of the card.

I would like the card to be clean yet important.

Im not sure if you include texture but i would like the named logo to be indented into the card etc.

show me something alive and free something thats clinical to the point yet has a feel of achievement. i would like people to go nice card.

Target Market(s)

high end clients, corporate, sports field manger, the guys that make the decisions

Industry/Entity Type

Business

Contact Information for Business Card

nformation to be included

Dorian Hesk (Director)
0487253916
dorian@tfcraft.biz
www.taddsfieldcrafts.com

instagram logo
google logo
facebook logo

Colors

Designer to choose colors to be used in the design.

Requirements
Nice to have
• indentations a really nice feel to the card good texture

```html
<!DOCTYPE html>
<html lang="en">
<head>
<meta charset="utf-8">
<title>Tadd's Field Crafts – Business Cards</title>
<link href="https://fonts.googleapis.com/css2?family=Roboto:wght@400;700;900&display=swap" rel="stylesheet">
<style>
  :root {
    --backdrop: #2a2a2c;
    --card: #ffffff;
    --card-edge: #e6e8ea;
    --brand-blue: #2a5c9e;
    --brand-blue-light: #3f8fd0;
    --brand-green: #2f9a4c;
    --ink-dark: #1b2f55;
    --white: #ffffff;
  }
  * { margin: 0; padding: 0; box-sizing: border-box; }
  html, body {
    width: 1200px; height: 997px; overflow: hidden;
    background: var(--backdrop);
    font-family: "Roboto", Arial, sans-serif;
  }
  .stage {
    position: relative; width: 1200px; height: 997px;
    display: flex; align-items: center; justify-content: center; gap: 60px;
  }
  .card {
    position: relative; width: 520px; height: 300px;
    background: var(--card);
    border: 1px solid var(--card-edge);
    box-shadow: 0 10px 30px rgba(0,0,0,.45);
    overflow: hidden;
  }
  .card svg.shapes { position: absolute; inset: 0; }
  .brand {
    position: absolute; left: 0; right: 0; text-align: center;
    color: var(--brand-blue); font-weight: 900; letter-spacing: .5px;
  }
  .card--front .brand { top: 128px; font-size: 30px; }
  .card--back .brand { top: 88px; font-size: 25px; }
  .band-label {
    position: absolute; color: var(--white); font-size: 13px;
    letter-spacing: 1.5px; text-transform: uppercase;
  }
  .band-label--residential { left: 40px; top: 213px; }
  .band-label--commercial { right: 40px; top: 213px; }
  .holder { position: absolute; left: 34px; top: 196px; color: var(--white); }
  .holder__name { font-size: 17px; font-weight: 700; letter-spacing: .5px; text-transform: uppercase; }
  .holder__role { font-size: 13px; font-weight: 700; color: var(--ink-dark); margin-left: 28px; }
  .contact {
    position: absolute; right: 44px; top: 144px; list-style: none;
    color: var(--white); font-size: 11px; text-align: right; line-height: 16px;
  }
  .contact__icons { position: absolute; right: 14px; top: 146px; }
  .website {
    position: absolute; right: 30px; top: 230px;
    color: var(--brand-blue); font-size: 13px; font-weight: 700; letter-spacing: 2px;
  }
</style>
</head>
<body>
<main class="stage">

  <section class="card card--front" aria-label="Card front">
    <svg class="shapes" width="520" height="300" viewBox="0 0 520 300">
      <circle cx="260" cy="88" r="30" fill="var(--brand-blue-light)"/>
      <line x1="0" y1="196" x2="520" y2="196" stroke="var(--brand-green)" stroke-width="1.5"/>
      <polygon points="0,202 290,202 270,242 0,242" fill="var(--brand-blue)"/>
      <polygon points="290,202 520,202 520,242 270,242" fill="var(--brand-green)"/>
      <line x1="0" y1="248" x2="520" y2="248" stroke="var(--brand-blue)" stroke-width="1.5"/>
    </svg>
    <p class="brand">TADD'S FIELD CRAFTS</p>
    <p class="band-label band-label--residential">Residential Services</p>
    <p class="band-label band-label--commercial">Commerical Services</p>
  </section>

  <section class="card card--back" aria-label="Card back">
    <svg class="shapes" width="520" height="300" viewBox="0 0 520 300">
      <circle cx="260" cy="52" r="26" fill="var(--brand-blue-light)"/>
      <polygon points="300,140 520,140 520,208 270,208" fill="var(--brand-green)"/>
      <line x1="270" y1="214" x2="520" y2="214" stroke="var(--brand-green)" stroke-width="1.5"/>
      <polygon points="0,178 270,178 240,258 0,258" fill="var(--brand-blue)"/>
      <line x1="0" y1="264" x2="520" y2="264" stroke="var(--brand-blue)" stroke-width="1.5"/>
      <circle cx="268" cy="196" r="52" fill="var(--white)"/>
      <circle cx="268" cy="196" r="46" fill="var(--brand-blue-light)" stroke="var(--brand-blue)" stroke-width="3"/>
    </svg>
    <p class="brand">TADD'S FIELD CRAFTS</p>
    <div class="holder">
      <p class="holder__name">Dorian Hesk</p>
      <p class="holder__role">Director</p>
    </div>
    <ul class="contact">
      <li>0487253916</li>
      <li>dorian@tfcraft.biz</li>
      <li>PO Box 318</li>
      <li>Kelvale B.C. QLD 4417</li>
    </ul>
    <svg class="contact__icons" width="18" height="50" viewBox="0 0 18 50" aria-hidden="true">
      <circle cx="9" cy="7" r="7" fill="var(--white)"/>
      <path d="M5 4 q1 -1 2 0 l1 2 -1 1 q1 2 3 3 l1 -1 2 1 q1 1 0 2 q-6 0 -8 -8z" fill="var(--brand-green)"/>
      <circle cx="9" cy="23" r="7" fill="var(--white)"/>
      <rect x="5" y="20" width="8" height="6" fill="none" stroke="var(--brand-green)" stroke-width="1.2"/>
      <path d="M5 20 l4 3 4 -3" fill="none" stroke="var(--brand-green)" stroke-width="1.2"/>
      <circle cx="9" cy="40" r="7" fill="var(--white)"/>
      <path d="M9 45 l-3 -5 a3 3 0 1 1 6 0z" fill="var(--brand-green)"/>
    </svg>
    <p class="website">www.taddsfieldcrafts.com</p>
  </section>

</main>
</body>
</html>
```